We are full service plumbing contractors that are capable of performing all of your plumbing need...

A clean, crisp website that conveys we can handle any plumbing from drain cleaning, repairs, to new construction. But emphasis on Leak detection, under-slab and underground water service leaks, repairs, and reroutes. Leak detection by acoustical, Thermal, or tracer gas , methods.Also emphasize advanced drain cleaning technologies and equipment. Don't just poke ahole in the drain blockage, Clean the pipe, with our High pressure hydrojetters, or Chain knocker drain cables that expand to the width of the pipe being cleaned.

Number of Pages Required

5+ page

Font styles to use
Sans Serif

Requirements
Should not have
• Canned photos

```html
<!DOCTYPE html>
<html lang="en">
<head>
<meta charset="utf-8">
<title>Reef Line Plumbing</title>
<link rel="stylesheet" href="https://fonts.googleapis.com/css2?family=Montserrat:wght@500;600;700;800&family=Open+Sans:wght@400;600;700&display=swap">
<style>
:root{
  --blue:#1e9ad6;
  --blue-dark:#1580b8;
  --red:#d6242a;
  --gold:#e9b51f;
  --ink:#222;
  --text:#555;
  --light:#efefef;
  --white:#fff;
  --night:#1b1b1b;
}
*{box-sizing:border-box;margin:0;padding:0}
html,body{width:1200px;height:4317px;overflow:hidden;background:var(--white)}
body{position:relative;font-family:"Open Sans",Arial,sans-serif;color:var(--text);font-size:13px}
.abs{position:absolute}
.heading{font-family:"Montserrat",Arial,sans-serif;font-weight:700;color:var(--ink);text-transform:uppercase}
.btn{position:absolute;display:flex;align-items:center;justify-content:center;color:var(--white);font-family:"Montserrat",Arial,sans-serif;font-weight:600;font-size:13px;text-transform:uppercase;letter-spacing:.5px}
.btn-blue{background:var(--blue)}
.btn-red{background:var(--red)}

/* header */
.topbar{top:0;left:0;width:1200px;height:86px;background:var(--white)}
.phone{top:22px;left:612px;display:flex;align-items:center;gap:8px;font-family:"Montserrat",sans-serif;font-weight:600;font-size:14px;color:var(--ink)}
.phone b{color:var(--blue)}
.phone-icon{width:28px;height:28px;border-radius:50%;border:2px solid var(--ink);display:flex;align-items:center;justify-content:center}
.social{top:22px;left:908px;display:flex;gap:8px}
.social span{width:26px;height:26px;border-radius:50%;border:2px solid var(--blue)}
.social.social-red span:last-child{border-color:var(--red)}
.navbar{top:86px;left:0;width:1200px;height:30px;background:var(--blue)}
.nav{top:86px;left:374px;height:30px;display:flex;align-items:center;gap:30px;font-family:"Montserrat",sans-serif;font-weight:600;font-size:12px;color:var(--white)}
.nav-quote{top:78px;left:900px;width:152px;height:44px}
.brand-panel{top:0;left:130px;width:218px;height:128px;background:var(--white);border-radius:0 0 18px 18px;display:flex;align-items:center;justify-content:center;gap:8px;box-shadow:0 4px 10px rgba(0,0,0,.12)}
.brand-mark{width:18px;height:18px;border-radius:50%;background:var(--red)}
.brand-name{font-family:"Montserrat",sans-serif;font-weight:800;font-size:22px;color:var(--red);line-height:1.05;text-transform:uppercase}

/* hero */
.hero{top:116px;left:0;width:1200px;height:580px;background:linear-gradient(135deg,#4a4f55 0%,#6c7278 40%,#2f3338 70%,#55595e 100%)}
.hero-title{top:272px;left:141px;font-family:"Montserrat",sans-serif;font-weight:800;font-size:38px;line-height:1.15;color:var(--white);text-transform:uppercase}
.hero-sub{top:372px;left:141px;font-size:15px;color:var(--white)}
.hero-call{top:414px;left:141px;width:150px;height:32px}
.quote-form{top:187px;left:711px;width:348px;height:345px;background:rgba(30,154,214,.88);padding:0 32px}
.quote-form h2{font-family:"Montserrat",sans-serif;font-weight:700;font-size:20px;color:var(--white);text-align:center;margin:14px 0 22px}
.field{height:42px;border-bottom:1px solid rgba(255,255,255,.6);display:flex;align-items:flex-end;padding-bottom:6px;font-size:10px;color:var(--white);letter-spacing:.5px}
.field.tall{height:54px}
.submit{position:relative;margin:30px auto 0;width:200px;height:30px}
.hero-wave{top:596px;left:0}

/* features */
.feature{top:806px;width:300px;text-align:center}
.feature-icon{width:100px;height:100px;border-radius:50%;margin:0 auto 22px;display:flex;align-items:center;justify-content:center}
.feature h3{font-family:"Montserrat",sans-serif;font-weight:700;font-size:15px;color:var(--ink);margin-bottom:6px}
.feature p{font-size:12px;line-height:1.5}

/* about */
.about{top:1094px;left:0;width:1200px;height:431px;background:var(--light)}
.about-title{top:1178px;left:141px;font-size:32px}
.about-title span{color:var(--blue)}
.about-text{top:1230px;left:141px;width:560px;font-size:12.5px;line-height:1.6}
.about-facts{top:1320px;left:141px;font-size:12.5px;font-weight:700;color:var(--ink);line-height:2}
.about-btn{top:1418px;left:141px;width:136px;height:32px}
.about-frame{top:1176px;left:744px;width:312px;height:296px;background:var(--gold)}
.about-video{top:1166px;left:754px;width:302px;height:288px;background:linear-gradient(180deg,#9db3c4 0%,#c9ced2 45%,#4e5a63 100%)}
.play{top:1280px;left:875px}

/* services */
.section-title{left:0;width:1200px;text-align:center;font-size:30px}
.section-title span{color:var(--blue)}
.divider{left:560px;width:80px;height:2px;background:var(--blue)}
.card{top:1756px;width:213px;height:282px;background:var(--white);box-shadow:0 2px 8px rgba(0,0,0,.15);text-align:center}
.card-photo{height:150px;background:linear-gradient(160deg,#7d8a94,#c4c9cc 60%,#5b656d)}
.card-icon{width:40px;height:40px;border-radius:50%;background:var(--blue);margin:-20px auto 8px;position:relative;border:3px solid var(--white)}
.card h3{font-family:"Montserrat",sans-serif;font-weight:700;font-size:14px;color:var(--ink);margin-bottom:6px}
.card p{font-size:11.5px;line-height:1.45;padding:0 14px}
.card-plus{position:absolute;bottom:-11px;left:95px;width:22px;height:22px;border-radius:50%;background:var(--blue);color:var(--white);font-weight:700;font-size:16px;line-height:22px}

/* why us */
.why{top:2135px;left:0;width:1200px;height:887px;background:linear-gradient(135deg,#2a2a2a 0%,#3b3d3f 40%,#1c1c1c 70%,#34373a 100%)}
.why-title{top:2196px;color:var(--white)}
.hub{top:2484px;left:478px;width:242px;height:242px;border-radius:50%;background:var(--white);border:8px solid var(--gold);display:flex;align-items:center;justify-content:center}
.hub .brand-name{font-size:26px;text-align:center}
.why-icon{width:86px;height:86px;border-radius:50%;background:var(--white);display:flex;align-items:center;justify-content:center}
.why-item{width:290px;text-align:center;color:var(--white)}
.why-item h3{font-family:"Montserrat",sans-serif;font-weight:700;font-size:15px;margin:14px 0 8px;text-transform:uppercase}
.why-item p{font-size:11.5px;line-height:1.5;color:#ddd}

/* testimonials */
.quote-card{top:3223px;width:445px;height:216px;background:var(--white);box-shadow:0 2px 10px rgba(0,0,0,.15);padding:24px 26px 0 60px}
.quote-bar{position:absolute;left:0;top:0;bottom:0;width:6px;background:var(--blue)}
.quote-mark{position:absolute;left:20px;top:14px;font-family:Georgia,serif;font-size:48px;color:var(--blue);line-height:1}
.quote-card p{font-style:italic;font-size:12.5px;line-height:1.6;color:#444}
.quote-card p b{color:var(--blue);font-style:normal}
.quote-foot{position:absolute;left:60px;right:26px;bottom:22px;display:flex;justify-content:space-between;border-top:1px solid #e2e2e2;padding-top:10px;font-weight:700;font-size:13px;color:var(--blue)}
.stars{color:var(--gold);letter-spacing:2px}
.arrow{top:3310px}

/* cta */
.cta-title{top:3646px;left:0;width:1200px;text-align:center;font-size:28px;line-height:1.2}
.cta-title span{color:var(--red)}

/* footer */
.footer{top:3986px;left:0;width:1200px;height:282px;background:var(--blue)}
.footer-wave{top:3880px;left:0}
.footer-brand{top:4030px;left:0;width:1200px;display:flex;justify-content:center;align-items:center;gap:8px}
.footer-brand .brand-name{color:var(--white)}
.footer-brand .brand-mark{background:var(--white)}
.footer-nav{top:4140px;left:0;width:1200px;display:flex;justify-content:center;gap:30px;font-family:"Montserrat",sans-serif;font-weight:600;font-size:12px;color:var(--white)}
.footer-contact{top:4190px;left:0;width:1200px;display:flex;justify-content:center;gap:60px;font-size:12px;color:var(--white)}
.footer-contact span{display:flex;align-items:center;gap:8px}
.bottom-bar{top:4268px;left:0;width:1200px;height:49px;background:var(--night);display:flex;align-items:center;justify-content:space-between;padding:0 141px;font-size:11px;color:#bbb}
.bottom-social{display:flex;gap:10px}
.bottom-social span{width:14px;height:14px;border-radius:50%;background:#bbb}
</style>
</head>
<body>

<!-- header -->
<div class="abs topbar"></div>
<div class="abs phone">
  <span class="phone-icon"><svg width="14" height="14" viewBox="0 0 24 24"><path d="M6.6 10.8a15 15 0 0 0 6.6 6.6l2.2-2.2c.3-.3.7-.4 1-.2 1.1.4 2.3.6 3.6.6.6 0 1 .4 1 1V20c0 .6-.4 1-1 1A17 17 0 0 1 3 4c0-.6.4-1 1-1h3.5c.6 0 1 .4 1 1 0 1.3.2 2.5.6 3.6.1.3 0 .7-.2 1z" fill="#222"/></svg></span>
  CALL OR TEXT NOW <b>808-555-0142</b>
</div>
<div class="abs social social-red"><span></span><span></span><span></span><span></span></div>
<div class="abs navbar"></div>
<nav class="abs nav"><span>HOME</span><span>ABOUT US</span><span>SERVICES</span><span>TEAM</span><span>BLOG</span><span>CONTACT US</span></nav>
<div class="btn btn-red nav-quote">Get a Quote</div>
<div class="abs brand-panel"><span class="brand-mark"></span><span class="brand-name">Reef Line<br>Plumbing</span></div>

<!-- hero -->
<div class="abs hero" role="img" aria-label="Plumber on site jetting water across a driveway"></div>
<h1 class="abs hero-title">Tired of waiting<br>for a plumber?</h1>
<p class="abs hero-sub">Call Us For A Fast Professional And Same Day Service</p>
<div class="btn btn-blue hero-call">Call Us Today</div>
<form class="abs quote-form">
  <h2>GET A QUOTE</h2>
  <div class="field">NAME</div>
  <div class="field">PHONE</div>
  <div class="field">EMAIL</div>
  <div class="field tall">HOW CAN WE HELP?</div>
  <div class="btn btn-red submit">Submit Inquiry</div>
</form>
<svg class="abs hero-wave" width="1200" height="100" viewBox="0 0 1200 100">
  <path d="M0 40 C250 100 450 0 700 40 S1050 70 1200 30 V100 H0Z" fill="#d9dcdf" opacity=".7"/>
  <path d="M0 70 C300 20 500 110 800 60 S1100 50 1200 70 V100 H0Z" fill="#fff"/>
</svg>

<!-- features -->
<div class="abs feature" style="left:138px">
  <div class="feature-icon" style="background:var(--gold)"><svg width="44" height="44" viewBox="0 0 24 24" fill="none" stroke="#fff" stroke-width="2"><path d="M12 3c3 4 6 7 6 11a6 6 0 0 1-12 0c0-4 3-7 6-11z"/></svg></div>
  <h3>NO-DIG DRAIN REPAIR</h3>
  <p>Lorem Ipsum is simply dummy text of<br>the printing and typesetting industry.</p>
</div>
<div class="abs feature" style="left:449px">
  <div class="feature-icon" style="background:var(--red)"><svg width="44" height="44" viewBox="0 0 24 24" fill="none" stroke="#fff" stroke-width="2"><path d="M14.7 6.3a4 4 0 0 0 5 5L12 19l-3 1 1-3 7.7-7.7M4 20l5-5"/></svg></div>
  <h3>REPAIRS ALL PIPE TYPES</h3>
  <p>Lorem Ipsum is simply dummy text of<br>the printing and typesetting industry.</p>
</div>
<div class="abs feature" style="left:757px">
  <div class="feature-icon" style="background:var(--blue)"><svg width="44" height="44" viewBox="0 0 24 24" fill="none" stroke="#fff" stroke-width="2"><circle cx="12" cy="12" r="9"/><path d="M12 7v5l3 2"/></svg></div>
  <h3>SAME DAY SERVICE</h3>
  <p>Lorem Ipsum is simply dummy text of<br>the printing and typesetting industry.</p>
</div>

<!-- about -->
<div class="abs about"></div>
<h2 class="abs heading about-title"><span>About</span> Reef Line</h2>
<p class="abs about-text">We are a group of experienced plumbers, that actually own the business. There is no "Passing the buck". We understand the importance of quality work, and satisfied customers. Our success is directly related to our performance, and your satisfaction.</p>
<p class="abs about-facts">Trusted Plumbing Contractors in West Hawaii.<br>Member Coastline Chamber of Commerce.<br>Past President Harbor Executive Association.</p>
<div class="btn btn-blue about-btn">Read More</div>
<div class="abs about-frame"></div>
<div class="abs about-video" role="img" aria-label="Team of plumbers standing beside their service van"></div>
<svg class="abs play" width="60" height="60" viewBox="0 0 60 60"><circle cx="30" cy="30" r="28" fill="rgba(0,0,0,.45)" stroke="#fff" stroke-width="3"/><path d="M24 18 L42 30 L24 42Z" fill="#fff"/></svg>

<!-- services -->
<h2 class="abs heading section-title" style="top:1630px"><span>Our</span> Services</h2>
<div class="abs divider" style="top:1686px"></div>
<div class="abs card" style="left:141px"><div class="card-photo" role="img" aria-label="Technician cleaning a drain line"></div><div class="card-icon"></div><h3>DRAIN CLEANING</h3><p>Lorem ipsum dolor sit amet consectetuer adipiscing elit, sed diam nonummy nibh eui.</p><span class="card-plus">+</span></div>
<div class="abs card" style="left:377px"><div class="card-photo" role="img" aria-label="New copper pipes during a reroute"></div><div class="card-icon"></div><h3>REPAIRS &amp; REROUTES</h3><p>Lorem ipsum dolor sit amet consectetuer adipiscing elit, sed diam nonummy nibh eui.</p><span class="card-plus">+</span></div>
<div class="abs card" style="left:610px"><div class="card-photo" role="img" aria-label="Thermal leak detection camera in use"></div><div class="card-icon"></div><h3>LEAK DETECTION</h3><p>Lorem ipsum dolor sit amet consectetuer adipiscing elit, sed diam nonummy nibh eui.</p><span class="card-plus">+</span></div>
<div class="abs card" style="left:843px"><div class="card-photo" role="img" aria-label="Plumbing rough-in on a new construction site"></div><div class="card-icon"></div><h3>NEW CONSTRUCTION</h3><p>Lorem ipsum dolor sit amet consectetuer adipiscing elit, sed diam nonummy nibh eui.</p><span class="card-plus">+</span></div>

<!-- why us -->
<div class="abs why" role="img" aria-label="Drain cleaning equipment and cables in a work truck"></div>
<h2 class="abs heading section-title why-title">Why Use Us?</h2>
<svg class="abs" style="top:2135px;left:0" width="1200" height="887" viewBox="0 0 1200 887">
  <g stroke="#fff" stroke-width="2" fill="none" opacity=".8">
    <path d="M354 254 C470 300 730 300 866 254"/>
    <path d="M365 620 C480 560 720 560 866 620"/>
    <path d="M311 300 L322 556"/>
    <path d="M909 300 L909 556"/>
  </g>
</svg>
<div class="abs hub"><span class="brand-name">Reef Line<br>Plumbing</span></div>
<div class="abs why-item" style="top:2346px;left:166px">
  <div class="why-icon" style="margin:0 auto"><svg width="40" height="40" viewBox="0 0 24 24" fill="none" stroke="#1e9ad6" stroke-width="2"><path d="M3 12l4-4 4 3 3-3 7 5-5 5-4-3-3 2z"/></svg></div>
  <h3>Experience</h3>
  <p>The 4 owners have been in the plumbing business in West Hawaii for the last 12 years. We are familiar with most of the condo complexes, as well as the subdivisions, and the plumbing issues that affect them.</p>
</div>
<div class="abs why-item" style="top:2346px;left:764px">
  <div class="why-icon" style="margin:0 auto"><svg width="40" height="40" viewBox="0 0 24 24" fill="none" stroke="#1e9ad6" stroke-width="2"><circle cx="12" cy="12" r="9"/><path d="M12 7v5l3 2"/></svg></div>
  <h3>Fast Response Times</h3>
  <p>We respond to many calls the same day, but can usually get there within 24 hours. If we can't, we will be honest with you, so that you can schedule someone who may be able to respond faster.</p>
</div>
<div class="abs why-item" style="top:2691px;left:177px">
  <div class="why-icon" style="margin:0 auto"><svg width="40" height="40" viewBox="0 0 24 24" fill="none" stroke="#1e9ad6" stroke-width="2"><path d="M14.7 6.3a4 4 0 0 0 5 5L12 19l-3 1 1-3 7.7-7.7M4 4l6 6M4 20l5-5"/></svg></div>
  <h3>Equipment</h3>
  <p>At Reef Line, we believe in investing in the latest cutting edge technology available to plumbers. We have the most effective drain cleaning equipment, video scoping, thermal imaging and electronic locating gear.</p>
</div>
<div class="abs why-item" style="top:2691px;left:764px">
  <div class="why-icon" style="margin:0 auto"><svg width="40" height="40" viewBox="0 0 24 24" fill="#1e9ad6"><circle cx="12" cy="8" r="3"/><circle cx="5" cy="10" r="2.2"/><circle cx="19" cy="10" r="2.2"/><path d="M6 19a6 6 0 0 1 12 0z"/></svg></div>
  <h3>Our Specialties</h3>
  <p>Water leak experts. Finding your water leak, inside or outside the house, can be expensive, but this is not always the best solution. We offer different options, including rerouting, adding new pipes, or simple repairing.</p>
</div>

<!-- testimonials -->
<h2 class="abs heading section-title" style="top:3096px"><span>Customer</span> Testimonials</h2>
<div class="abs divider" style="top:3150px"></div>
<svg class="abs arrow" style="left:92px" width="16" height="40" viewBox="0 0 16 40"><path d="M14 2 L2 20 L14 38" stroke="#ccc" stroke-width="2" fill="none"/></svg>
<svg class="abs arrow" style="left:1092px" width="16" height="40" viewBox="0 0 16 40"><path d="M2 2 L14 20 L2 38" stroke="#ccc" stroke-width="2" fill="none"/></svg>
<div class="abs quote-card" style="left:141px"><span class="quote-bar"></span><span class="quote-mark">&ldquo;</span>
  <p>"After our water bill was getting larger and larger, I contacted Keoni. He immediately made an appt. to check out the problem the very next day. He arrived with Malia and they determined it was the main water line." <b>[+]</b></p>
  <div class="quote-foot"><span>Joanne M.</span><span class="stars">★★★★★</span></div></div>
<div class="abs quote-card" style="left:611px"><span class="quote-bar"></span><span class="quote-mark">&ldquo;</span>
  <p>"After receiving our water bill and about choking (it had gone up over $200) we thought.....we must have a leak. My husband and I did our own troubleshooting and came to the conclusion that we had a leak" <b>[+]</b></p>
  <div class="quote-foot"><span>Mahalo Keoni &amp; Malia!!!!</span><span class="stars">★★★★★</span></div></div>
<div class="btn btn-blue" style="top:3470px;left:510px;width:180px;height:34px">See More Reviews</div>

<!-- call to action -->
<h2 class="abs heading cta-title"><span>Trusted Plumbing</span><br>Contractors in West Hawaii.</h2>
<div class="btn btn-blue" style="top:3740px;left:437px;width:124px;height:32px">Call Us Today</div>
<div class="btn btn-red" style="top:3740px;left:580px;width:120px;height:32px">Get a Quote</div>

<!-- footer -->
<svg class="abs footer-wave" width="1200" height="110" viewBox="0 0 1200 110">
  <path d="M0 40 C250 0 500 90 800 40 S1100 10 1200 30 V110 H0Z" fill="#8fd0ef"/>
  <path d="M0 70 C300 30 600 110 900 60 S1150 50 1200 60 V110 H0Z" fill="#1e9ad6"/>
</svg>
<div class="abs footer"></div>
<div class="abs footer-brand"><span class="brand-mark"></span><span class="brand-name">Reef Line Plumbing</span></div>
<nav class="abs footer-nav"><span>HOME</span><span>ABOUT US</span><span>SERVICES</span><span>TEAM</span><span>BLOG</span><span>CONTACT US</span></nav>
<div class="abs footer-contact">
  <span><svg width="12" height="16" viewBox="0 0 12 16"><path d="M6 0a6 6 0 0 1 6 6c0 4-6 10-6 10S0 10 0 6a6 6 0 0 1 6-6z" fill="#fff"/><circle cx="6" cy="6" r="2" fill="#1e9ad6"/></svg>12 Harbor Road, Kailua-Kona, HI 96740</span>
  <span><svg width="14" height="14" viewBox="0 0 24 24"><path d="M6.6 10.8a15 15 0 0 0 6.6 6.6l2.2-2.2c.3-.3.7-.4 1-.2 1.1.4 2.3.6 3.6.6.6 0 1 .4 1 1V20c0 .6-.4 1-1 1A17 17 0 0 1 3 4c0-.6.4-1 1-1h3.5c.6 0 1 .4 1 1 0 1.3.2 2.5.6 3.6.1.3 0 .7-.2 1z" fill="#fff"/></svg>808-555-0142</span>
  <span><svg width="16" height="12" viewBox="0 0 16 12"><rect x="0.5" y="0.5" width="15" height="11" fill="none" stroke="#fff"/><path d="M1 1l7 6 7-6" fill="none" stroke="#fff"/></svg>info@reeflineplumbing.com</span>
</div>
<div class="abs bottom-bar"><span>Copyright © 2019 REEF LINE PLUMBING. All Rights Reserved.</span><span class="bottom-social"><span></span><span></span><span></span></span></div>

</body>
</html>
```